Business Card Design

Velora Pixel Outreach

An online marketing consulting & strategy business for the cosmetic niche

We specialise in Increasing Leads, Conversions & Content Marketing

I am looking for a very clean, BOLD business card that is simple & effective

Target Market(s)

cosmetic surgeons & cosmetic clinics

Industry/Entity Type

Marketing

Contact Information for Business Card

Brett Kaminski
Online Marketing Strategist

Brett@VeloraPixelOutreach.example
0491 268 530

LinkedIn: in/brettkaminski

```html
<!DOCTYPE html>
<html lang="en">
<head>
<meta charset="utf-8">
<title>Velora Pixel Outreach – Business Card</title>
<link rel="stylesheet" href="https://fonts.googleapis.com/css2?family=Exo+2:wght@500&family=Open+Sans:wght@400;700&display=swap">
<style>
  :root {
    --backdrop: #9a9a9a;
    --brand-blue: #00adef;
    --card-white: #ffffff;
    --wordmark-grey: #5b5b5d;
    --ink: #1a1a1a;
    --shadow: rgba(0, 0, 0, 0.25);
  }
  * { box-sizing: border-box; margin: 0; padding: 0; }
  html, body {
    width: 1200px;
    height: 900px;
    overflow: hidden;
  }
  body {
    background: var(--backdrop);
    position: relative;
    font-family: "Open Sans", Arial, sans-serif;
  }
  .card {
    position: absolute;
    width: 540px;
    height: 310px;
    box-shadow: 0 10px 30px var(--shadow);
  }
  .card--front {
    left: 70px;
    top: 110px;
    background: var(--brand-blue);
    display: flex;
    align-items: center;
    justify-content: center;
  }
  .card--back {
    left: 590px;
    top: 480px;
    background: var(--card-white);
  }
  .lockup {
    display: flex;
    align-items: center;
    gap: 14px;
  }
  .lockup__mark {
    border-radius: 50%;
    flex: none;
  }
  .lockup__name {
    font-family: "Exo 2", Arial, sans-serif;
    font-weight: 500;
    text-transform: uppercase;
    line-height: 0.98;
    letter-spacing: 0.08em;
  }
  .card--front .lockup__mark {
    width: 64px; height: 64px;
    background: var(--card-white);
  }
  .card--front .lockup__name {
    color: var(--card-white);
    font-size: 30px;
  }
  .card--back .lockup {
    position: absolute;
    left: 26px;
    top: 22px;
  }
  .card--back .lockup__mark {
    width: 58px; height: 58px;
    background: var(--brand-blue);
  }
  .card--back .lockup__name {
    color: var(--wordmark-grey);
    font-size: 27px;
  }
  .contact {
    position: absolute;
    left: 32px;
    top: 150px;
  }
  .contact__name {
    color: var(--brand-blue);
    font-weight: 700;
    font-size: 17px;
    text-transform: uppercase;
    letter-spacing: 0.02em;
  }
  .contact__title {
    color: var(--ink);
    font-size: 12px;
    margin-top: 2px;
  }
  .contact__list {
    list-style: none;
    margin-top: 26px;
  }
  .contact__item {
    display: flex;
    align-items: center;
    gap: 8px;
    color: var(--ink);
    font-size: 12px;
    line-height: 1.5;
  }
  .contact__icon { width: 12px; height: 12px; flex: none; }
  .decor-ring {
    position: absolute;
    right: 36px;
    bottom: 28px;
    width: 170px;
    height: 170px;
    border-radius: 50%;
    border: 22px solid var(--brand-blue);
  }
</style>
</head>
<body>
  <section class="card card--front" aria-label="Business card front">
    <div class="lockup">
      <span class="lockup__mark"></span>
      <p class="lockup__name">Velora<br>Pixel<br>Outreach</p>
    </div>
  </section>

  <section class="card card--back" aria-label="Business card back">
    <div class="lockup">
      <span class="lockup__mark"></span>
      <p class="lockup__name">Velora<br>Pixel<br>Outreach</p>
    </div>

    <div class="contact">
      <h1 class="contact__name">Brett Kaminski</h1>
      <p class="contact__title">Online Marketing Strategist</p>
      <ul class="contact__list">
        <li class="contact__item">
          <svg class="contact__icon" viewBox="0 0 12 12" aria-hidden="true">
            <circle cx="6" cy="6" r="6" fill="var(--brand-blue)"/>
            <rect x="4" y="2.5" width="4" height="7" rx="0.8" fill="none" stroke="#fff" stroke-width="1"/>
          </svg>
          0491 268 530
        </li>
        <li class="contact__item">
          <svg class="contact__icon" viewBox="0 0 12 12" aria-hidden="true">
            <circle cx="6" cy="6" r="6" fill="var(--brand-blue)"/>
            <rect x="2.8" y="3.8" width="6.4" height="4.4" fill="none" stroke="#fff" stroke-width="0.9"/>
            <path d="M2.8 3.8 L6 6.4 L9.2 3.8" fill="none" stroke="#fff" stroke-width="0.9"/>
          </svg>
          Brett@VeloraPixelOutreach.example
        </li>
        <li class="contact__item">
          <svg class="contact__icon" viewBox="0 0 12 12" aria-hidden="true">
            <circle cx="6" cy="6" r="6" fill="var(--brand-blue)"/>
          </svg>
          in/brettkaminski
        </li>
      </ul>
    </div>

    <span class="decor-ring" aria-hidden="true"></span>
  </section>
</body>
</html>
```